I need a business card for myself, being a proprietor of a funeral parlor based in Manila. I'd like the card to have either of the following:
White Font on Black Background
or
Black Font on White Background
No logo is needed however I will appreciate any efforts to show a symbol of eternal happiness, aptly designed with above mentioned colors in mind.
Company name, address and contact on the lower right corner.
Logo or symbol anywhere.
Quillstone Funeral Services
+639174826351
darvik4521@pelmora.com
corner of Brisco Avenue and Velhurst Street
Makati City, Philippines
Thank you.
Update: Please include a small dove in your design. You are free to choose where you would like it on the card.

```html
<!DOCTYPE html>
<html lang="en">
<head>
<meta charset="UTF-8">
<title>Quillstone Funeral Services – Business Card</title>
<link href="https://fonts.googleapis.com/css2?family=Lato:wght@400;700&display=swap" rel="stylesheet">
<style>
  :root {
    --backdrop-light: #f4f4f4;
    --backdrop-dark: #c9c9c9;
    --card-white: #ffffff;
    --card-black: #0c0c0c;
    --ink-dark: #1a1a1a;
    --ink-light: #ffffff;
  }
  html, body {
    margin: 0;
    width: 1200px;
    height: 900px;
    overflow: hidden;
  }
  body {
    background: radial-gradient(ellipse at 50% 45%, var(--backdrop-light) 0%, var(--backdrop-dark) 100%);
    font-family: "Lato", sans-serif;
    position: relative;
  }
  .business-card {
    position: absolute;
    left: 180px;
    top: 210px;
    width: 840px;
    height: 480px;
    background: var(--card-white);
    box-shadow: 0 18px 40px rgba(0,0,0,0.25);
    overflow: hidden;
  }
  .card-band {
    position: absolute;
    left: 0;
    right: 0;
    top: 180px;
    bottom: 0;
    background: var(--card-black);
  }
  .company-name {
    position: absolute;
    right: 48px;
    top: 132px;
    margin: 0;
    font-size: 29px;
    font-weight: 700;
    color: var(--ink-dark);
    letter-spacing: -0.5px;
  }
  .brand-name {
    position: absolute;
    left: 48px;
    top: 212px;
    margin: 0;
    display: flex;
    align-items: center;
    gap: 14px;
    font-size: 34px;
    font-weight: 700;
    color: var(--ink-light);
  }
  .brand-dot {
    width: 30px;
    height: 30px;
    border-radius: 50%;
    background: var(--ink-light);
  }
  .contact-block {
    position: absolute;
    right: 48px;
    top: 218px;
    text-align: right;
    color: var(--ink-light);
    font-size: 24px;
    line-height: 1.3;
  }
  .contact-block p { margin: 0; }
  .contact-email {
    margin-top: 22px !important;
    display: flex;
    align-items: center;
    justify-content: flex-end;
    gap: 10px;
  }
  .contact-phone {
    position: absolute;
    left: 40px;
    bottom: 48px;
    margin: 0;
    color: var(--ink-light);
    font-size: 28px;
    display: flex;
    align-items: center;
    gap: 12px;
  }
  .icon { fill: var(--ink-light); }
</style>
</head>
<body>
  <div class="business-card">
    <div class="card-band"></div>

    <h1 class="company-name">Quillstone Funeral Services</h1>

    <p class="brand-name"><span class="brand-dot"></span>Quillstone</p>

    <div class="contact-block">
      <p>Corner of Brisco Avenue,&amp;</p>
      <p>Velhurst Street Makati City, Philippines</p>
      <p class="contact-email">
        <svg class="icon" width="24" height="17" viewBox="0 0 24 17" aria-hidden="true">
          <rect x="0" y="0" width="24" height="17" rx="1"/>
          <path d="M1 1 L12 10 L23 1" fill="none" stroke="#0c0c0c" stroke-width="2"/>
        </svg>
        darvik4521@pelmora.com
      </p>
    </div>

    <p class="contact-phone">
      <svg class="icon" width="26" height="20" viewBox="0 0 26 20" aria-hidden="true">
        <path d="M1 6 C1 1 25 1 25 6 L25 8 L19 8 L19 5 L7 5 L7 8 L1 8 Z"/>
        <path d="M6 9 L20 9 L24 19 L2 19 Z"/>
      </svg>
      +639174826351
    </p>
  </div>
</body>
</html>
```